A start-up named "Corvath Therapeutics" - needs a new PowerPoint design

We need a new PowerPoint Design for an early-stage start-up named "Corvath Therapeutics" seeking to disrupt the current approach towards drug discovery within aging disorders.

We would like to build on Corvath's legacy, the founder of the modern science of genetics, by employing a multidisciplinary approach, experimenting, and providing elderly patients the attention they deserve.

We have selected the suffix "therapeutics" intentionally as it stands for (a medicine) the treatment of disease; the science of healing. Alzheimer’s treatment is a huge, urgent, unmet need:
- Shift from a disease-management system to a preventive medicine system
- Focus on increasing the health span, not only the life span

Target Market(s)

Pharma/ Biotech Executives Medical Institutions Healthcare professionals (MDs, nurses, payors, pharmacists, etc.) Patients

Industry/Entity Type

Healthcare

Other font styles liked:
• Celias

Colors
0054AA
0677BA
7BADD7
CADEEF
E8F1F8
E54698
E96AAD
F1A4CE
F9D9EA
FCEFF6
A7469A
B969AE
D3A5CF
EDDBEB
F8F0F9
6B429C
8869AF
B7A5CE
E3DAEB
F3F0F8

Requirements
Must have
• - differentiate from other companies named after Corvath - differentiate from other Pharma/ Biotech companies
Nice to have
• simplicity/ minimalist logo vivid colors gradient 3D Life-Sciences inspired Simple geometry Balance
Should not have
• mascot/ emblem watermark logo animated ink style nature-inspired inventive typography artistic chaos

```html
<!DOCTYPE html>
<html lang="en">
<head>
<meta charset="utf-8">
<title>Corvath Therapeutics – Slide Template Part 2</title>
<link rel="stylesheet" href="https://fonts.googleapis.com/css2?family=Outfit:wght@400;500;600;700&family=Arimo:wght@400;700&display=swap">
<style>
  :root {
    --bg: #f2f2f2;
    --white: #ffffff;
    --blue-deep: #0054aa;
    --blue-mid: #0677ba;
    --blue-soft: #3f82c2;
    --blue-dark: #3560b0;
    --pink: #e54698;
    --pink-deep: #c8336e;
    --purple: #6b429c;
    --purple-mid: #7b3aa0;
    --row-alt: #f1f1f1;
    --ink: #1a1a1a;
    --rule: #c8c8c8;
    --label-blue: #0000ff;
  }
  * { margin: 0; padding: 0; box-sizing: border-box; }
  html, body { width: 1200px; height: 1200px; overflow: hidden; }
  body { background: var(--bg); position: relative; font-family: "Outfit", sans-serif; }

  .slide { position: absolute; left: 176px; width: 846px; height: 477px; background: var(--white); overflow: hidden; }
  .slide--table { top: 42px; }
  .slide--closing { top: 547px; height: 476px; }

  .top-bar { position: absolute; left: 0; top: 0; width: 100%; height: 5px;
    background: linear-gradient(90deg, var(--pink-deep), var(--purple-mid)); }

  .slide-title { position: absolute; left: 27px; top: 30px; font-size: 27px; font-weight: 600; color: var(--blue-deep); letter-spacing: 0.2px; }

  .data-table { position: absolute; left: 26px; top: 94px; width: 793px; border-collapse: collapse; table-layout: fixed; }
  .data-table th, .data-table td { height: 50px; text-align: left; padding-left: 7px; vertical-align: middle; }
  .data-table thead th { height: 49px; background: var(--pink); color: var(--white); font-weight: 600; font-size: 16.5px; }
  .data-table col.col-label { width: 99px; }
  .data-table col.col-value { width: 99.14px; }
  .data-table tbody tr:nth-child(even) { background: var(--row-alt); }
  .data-table tbody th { color: var(--blue-deep); font-weight: 700; font-size: 16.5px; }
  .data-table tbody td { font-family: "Arimo", sans-serif; font-size: 16px; color: var(--ink); }
  .data-table tbody tr:last-child th, .data-table tbody tr:last-child td { border-bottom: 2px solid var(--pink); }

  .brand { position: absolute; display: flex; align-items: center; color: var(--blue-mid); font-weight: 500; }
  .brand-mark { background: var(--blue-mid); flex: none; }
  .brand--footer { left: 26px; top: 436px; gap: 6px; font-size: 14px; }
  .brand--footer .brand-mark { width: 20px; height: 20px; }
  .brand--hero { left: 30px; top: 52px; gap: 12px; font-size: 27px; line-height: 1.05; }
  .brand--hero .brand-mark { width: 52px; height: 52px; }

  .footer-band { position: absolute; right: 0; bottom: 0; width: 216px; height: 33px; }
  .footer-text { position: absolute; left: 677px; top: 455px; font-size: 9.5px; line-height: 12px; color: var(--white); white-space: nowrap; }
  .footer-text .sep { display: inline-block; width: 1px; height: 11px; background: var(--white); margin: 0 6px -2px 8px; }
  .footer-text .page { font-weight: 700; }

  .closing-art { position: absolute; left: 0; top: 0; width: 846px; height: 476px; }
  .thanks { position: absolute; left: 28px; top: 160px; font-size: 77px; font-weight: 700; color: var(--blue-deep); letter-spacing: -0.5px; line-height: 1; }
  .divider { position: absolute; left: 30px; top: 261px; width: 393px; height: 1px; background: var(--rule); }
  .tagline { position: absolute; left: 30px; top: 273px; font-size: 15.5px; color: #333; }

  .part-label { position: absolute; left: 0; top: 1068px; width: 458px; height: 108px; background: var(--label-blue);
    color: var(--white); font-family: "Arimo", sans-serif; font-weight: 700; font-size: 76px; line-height: 108px; padding-left: 48px; }
</style>
</head>
<body>

<section class="slide slide--table">
  <div class="top-bar"></div>
  <h1 class="slide-title">Table Slide</h1>
  <table class="data-table">
    <colgroup>
      <col class="col-label"><col class="col-value"><col class="col-value"><col class="col-value"><col class="col-value"><col class="col-value"><col class="col-value"><col class="col-value">
    </colgroup>
    <thead>
      <tr><th>Data</th><th>Header</th><th>Header</th><th>Header</th><th>Header</th><th>Header</th><th>Header</th><th>Header</th></tr>
    </thead>
    <tbody>
      <tr><th>Value</th><td>00</td><td>00</td><td>00</td><td>00</td><td>00</td><td>00</td><td>00</td></tr>
      <tr><th>Value</th><td>00</td><td>00</td><td>00</td><td>00</td><td>00</td><td>00</td><td>00</td></tr>
      <tr><th>Value</th><td>00</td><td>00</td><td>00</td><td>00</td><td>00</td><td>00</td><td>00</td></tr>
      <tr><th>Value</th><td>00</td><td>00</td><td>00</td><td>00</td><td>00</td><td>00</td><td>00</td></tr>
      <tr><th>Value</th><td>00</td><td>00</td><td>00</td><td>00</td><td>00</td><td>00</td><td>00</td></tr>
    </tbody>
  </table>

  <div class="brand brand--footer"><span class="brand-mark"></span><span>Corvath</span></div>

  <svg class="footer-band" viewBox="0 0 216 33" aria-hidden="true">
    <defs>
      <linearGradient id="bandGrad" x1="0" x2="1" y1="0" y2="0">
        <stop offset="0" stop-color="#c8336e"/>
        <stop offset="1" stop-color="#7b3aa0"/>
      </linearGradient>
    </defs>
    <polygon points="19,0 216,0 216,33 0,33" fill="#0054aa"/>
    <polygon points="33,0 216,0 216,33 14,33" fill="url(#bandGrad)"/>
  </svg>
  <div class="footer-text">Copywrite Statement 2022<span class="sep"></span><span class="page">7</span></div>
</section>

<section class="slide slide--closing">
  <svg class="closing-art" viewBox="0 0 846 476">
    <defs>
      <linearGradient id="photoGrad" x1="0" x2="0" y1="0" y2="1">
        <stop offset="0" stop-color="#3f9be0"/>
        <stop offset="0.45" stop-color="#8a8fd0"/>
        <stop offset="0.75" stop-color="#c77bb6"/>
        <stop offset="1" stop-color="#c8336e"/>
      </linearGradient>
    </defs>
    <polygon role="img" aria-label="Photo of a scientist in a lab coat and safety glasses examining a test tube in a laboratory" points="579,0 846,0 846,476 365,476" fill="url(#photoGrad)"/>
    <line x1="562" y1="0" x2="490" y2="171" stroke="#0677ba" stroke-width="2.5"/>
    <polygon points="404,342 433,342 376,476 344,476" fill="#3f82c2"/>
    <polygon points="433,342 463,342 404,476 376,476" fill="#3560b0"/>
  </svg>

  <div class="brand brand--hero"><span class="brand-mark"></span><span>Corvath<br>Therapeutics</span></div>
  <h2 class="thanks">Thank You!</h2>
  <div class="divider"></div>
  <p class="tagline">Lorem ipsum dolor sit amet, consectetur adipiscing elit.</p>
</section>

<div class="part-label">PART 2</div>

</body>
</html>
```